New Business Card Design Project

New business card design required for an electrical business in Australia. Offering quality electrical services including design and installation. Electrical services offered are domestic, commercial and industrial. Also meets all the air conditioning installation and maintenance needs.

Target Market(s)

The business is sleek, professional and caters primarily to wealthy clients and government contracts looking for exceptional, tailored service.

Industry/Entity Type

Electrical

Contact Information for Business Card

Gareth Pollwick (Director)
0438 692 174
admin@rvoelectrical.com.au
www.rvoelectrical.com.au

Font styles to use
Sans Serif

Requirements
Must have
• The business card must show the license number - 64139 to comply with legislation.
Nice to have
• The logo colours and fonts could be incorporated into the design if the designer sees fit. We are open to new ideas and welcome creativity. The logo style guide is attached for reference if required.

```html
<!DOCTYPE html>
<html lang="en">
<head>
<meta charset="utf-8">
<title>RVO Electrical – Business Card</title>
<link rel="stylesheet" href="https://fonts.googleapis.com/css2?family=Montserrat:wght@300;400;500;800&display=swap">
<style>
  :root {
    --navy: #112b55;
    --white: #ffffff;
    --ink: #3c3c3c;
    --rule: #5a5a5a;
    --silver: #c9ccd2;
    --backdrop: #2a2a2a;
  }
  * { margin: 0; padding: 0; box-sizing: border-box; }
  html, body { width: 1200px; height: 895px; overflow: hidden; }
  body {
    background: var(--backdrop);
    font-family: "Montserrat", sans-serif;
    display: flex;
    align-items: center;
    justify-content: center;
    gap: 40px;
  }
  .card {
    width: 540px;
    height: 310px;
    border-radius: 26px;
    position: relative;
    overflow: hidden;
  }
  .card-front {
    background: var(--navy);
    display: flex;
    align-items: center;
    justify-content: center;
  }
  .brand {
    display: flex;
    align-items: center;
    gap: 12px;
    font-weight: 500;
    letter-spacing: 0.12em;
    text-transform: uppercase;
  }
  .brand-mark {
    width: 14px; height: 14px;
    border-radius: 50%;
    display: inline-block;
  }
  .card-front .brand { color: var(--silver); font-size: 34px; }
  .card-front .brand-mark { background: var(--silver); width: 18px; height: 18px; }

  .card-back { background: var(--white); }
  .card-back .brand {
    position: absolute; top: 34px; left: 0; right: 0;
    justify-content: center;
    color: var(--navy); font-size: 26px;
  }
  .card-back .brand-mark { background: var(--navy); }

  .identity {
    position: absolute; top: 98px; left: 28px; right: 28px;
    display: flex; align-items: center; gap: 14px;
  }
  .identity .rule { flex: 1; height: 1px; background: var(--rule); }
  .identity-text { text-align: center; }
  .person-name {
    color: var(--navy); font-weight: 800; font-size: 22px; letter-spacing: 0.02em;
    text-transform: uppercase;
  }
  .person-role { color: var(--ink); font-weight: 300; font-size: 13px; margin-top: 2px; letter-spacing: 0.04em; }

  .contacts {
    position: absolute; top: 172px; left: 18px; right: 18px;
    display: flex; justify-content: space-between;
  }
  .contact {
    flex: 1; display: flex; flex-direction: column; align-items: center; gap: 8px;
    color: var(--ink); font-size: 11.5px; font-weight: 400;
  }
  .contact-icon { width: 30px; height: 30px; }

  .license-band {
    position: absolute; left: 0; right: 0; bottom: 0; height: 52px;
    background: var(--navy); color: var(--white);
    display: flex; align-items: center; justify-content: center;
    font-weight: 500; font-size: 14px; letter-spacing: 0.04em;
  }
</style>
</head>
<body>
  <section class="card card-front">
    <div class="brand"><span class="brand-mark"></span><span class="brand-name">RVO Electrical</span></div>
  </section>

  <section class="card card-back">
    <div class="brand"><span class="brand-mark"></span><span class="brand-name">RVO Electrical</span></div>

    <div class="identity">
      <span class="rule"></span>
      <div class="identity-text">
        <p class="person-name">Gareth Pollwick</p>
        <p class="person-role">Director</p>
      </div>
      <span class="rule"></span>
    </div>

    <div class="contacts">
      <div class="contact">
        <svg class="contact-icon" viewBox="0 0 30 30" aria-hidden="true">
          <circle cx="15" cy="15" r="13.5" fill="none" stroke="#3c3c3c" stroke-width="1.2"/>
          <path d="M9.5 11.5c0 5 4 9 9 9l2-2.2-2.6-1.8-1.4 1.2c-1.8-.8-3.3-2.3-4.1-4.1l1.2-1.4-1.8-2.6z" fill="#112b55"/>
        </svg>
        <span>0438 692 174</span>
      </div>
      <div class="contact">
        <svg class="contact-icon" viewBox="0 0 30 30" aria-hidden="true">
          <circle cx="15" cy="15" r="13.5" fill="none" stroke="#3c3c3c" stroke-width="1.2"/>
          <rect x="8" y="10" width="14" height="10" rx="1.5" fill="#112b55"/>
          <path d="M8.5 10.8 15 15.6l6.5-4.8" fill="none" stroke="#fff" stroke-width="1.2"/>
        </svg>
        <span>admin@rvoelectrical.com.au</span>
      </div>
      <div class="contact">
        <svg class="contact-icon" viewBox="0 0 30 30" aria-hidden="true">
          <circle cx="15" cy="15" r="13.5" fill="none" stroke="#3c3c3c" stroke-width="1.2"/>
          <circle cx="15" cy="15" r="7" fill="#112b55"/>
          <g fill="none" stroke="#fff" stroke-width="0.8">
            <ellipse cx="15" cy="15" rx="3" ry="7"/>
            <path d="M8 15h14M9 11.5h12M9 18.5h12M15 8v14"/>
          </g>
        </svg>
        <span>rvoelectrical.com.au</span>
      </div>
    </div>

    <div class="license-band">License # 64139</div>
  </section>
</body>
</html>
```